Book Cover Design Project

NOTE. I need the design in four days of posting this!

This will be the cover of my first book, WALK THE HIGH LINE -
alchemy in the real business world. The book explains defines what Purpose and Meaning is, and how to use it in business. I have included the first chapter to provide a background.

I want the core colours to be black and white, and use the colours Violet, Cerulean Blue Extra Pale (powder blue), Cadmium Lemon (flouro yellow). I plan on using this design as the basis for future books in the WALK THE HIGH LINE series, where the yellow is carried through but the violet and blue colours changing.

This is a spiritual business book without using any spiritual language. It is strongly masculine and direct in its nature.

What I am looking for is something Remarkable that captures my reader immediately. My reader is a seeker. He/she is an entrepreneur perhaps looking to setup a new venture and looking for new and better ways of doing things, or he/she may be a small/medium business owner perhaps bored looking for more meaning in personal and business life), or the corporate person who is looking to get out and do something new. Age 35-50.
Updates

Hi I want to correct the paper size. It is "C Format" (trade paperbacks) are 135mm x 216mm (5.32" x 8.51").

Thks

Reason: A deadline has changed which means the completion of this book cover is less time-critical.

This is a business book that introduces new concepts, such as Purpose. Although it is based on spiritual principals  it is using normal business language when explaining what Purpose is, and how businesses can identify it and use it to be more successful.

If there is a border between a self-help and a business book, this book sits close to the border but markedly on the business side.

Hi I want to confirm the book size. The book size I require is the Australian C Format, which measures 153mm W x 234mm H. 

Sorry for any confusion

Reason: Hi I have extended the deadline as I want to be able to print prospective covers and see how they look like in a bookshop next to other covers.

Reason: To allow for final negotiations.

Industry/Entity Type

Business

```html
<!DOCTYPE html>
<html lang="en">
<head>
<meta charset="utf-8">
<title>Walk the High Line – Book Cover</title>
<link rel="stylesheet" href="https://fonts.googleapis.com/css2?family=Libre+Franklin:wght@300;700&display=swap">
<style>
  :root {
    --stage: #ffffff;
    --cover-black: #231f20;
    --bubble-grey: #4a4a4a;
    --text-white: #ffffff;
    --accent-blue: #00a6e6;
    --accent-magenta: #e6127e;
    --accent-yellow: #fff200;
  }

  * { margin: 0; padding: 0; box-sizing: border-box; }

  html, body {
    width: 1200px;
    height: 900px;
    overflow: hidden;
    background: var(--stage);
  }

  .stage {
    width: 1200px;
    height: 900px;
    display: flex;
    justify-content: center;
    align-items: center;
  }

  .book-cover {
    position: relative;
    width: 588px;
    height: 900px;
    background: var(--cover-black);
    overflow: hidden;
  }

  .cover-heading {
    position: absolute;
    top: 64px;
    left: 55px;
  }

  .author-name {
    font-family: "Libre Franklin", Arial, sans-serif;
    font-weight: 300;
    font-size: 19px;
    color: var(--text-white);
    letter-spacing: 0.2px;
  }

  .book-title {
    display: inline-block;
    margin-top: 10px;
    padding-bottom: 6px;
    font-family: "Libre Franklin", Arial, sans-serif;
    font-weight: 700;
    font-size: 35px;
    line-height: 1.1;
    color: var(--text-white);
    border-bottom: 8px solid var(--accent-blue);
  }

  .cover-artwork {
    position: absolute;
    left: 0;
    top: 190px;
    width: 588px;
    height: 710px;
    background:
      radial-gradient(ellipse 45% 35% at 58% 32%, rgba(255, 242, 0, 0.35), transparent 70%),
      radial-gradient(ellipse 45% 40% at 38% 50%, rgba(0, 166, 230, 0.35), transparent 70%),
      radial-gradient(ellipse 90% 25% at 45% 82%, rgba(230, 18, 126, 0.45), transparent 75%),
      linear-gradient(180deg, var(--cover-black) 0%, var(--bubble-grey) 55%, var(--cover-black) 100%);
  }
</style>
</head>
<body>
  <main class="stage">
    <article class="book-cover">
      <header class="cover-heading">
        <p class="author-name">Anders Holmqvist</p>
        <h1 class="book-title">WALK THE HIGH LINE</h1>
      </header>
      <div class="cover-artwork" role="img" aria-label="Abstract illustration of yellow and blue arrows sweeping upward over magenta wave lines and grey bubbles"></div>
    </article>
  </main>
</body>
</html>
```